seeking a modern Business Card design for Roof Plumbering Business

wexcombe roof plumbing is a local metal re-roof and new construction specialist. We are seeking a modern business card to assist with networking within the industry. Our services are predominantly the installation of metal roofs on new houses, however we also do re-roofs when an existing roof needs replacing. We service both residential and commercial properties. Please include the below details on the card:
Name: Owen Wexcombe
Phone: 0471 385 962
Email: owenwexcomberoofing@mailnest.example

Residential & Commercial
Re-roof & New Construction
Fully Insured

I have uploaded our business logo, which we think would suit a black background. Please use all lower case for business name.
Cheers
Updates

Hey Guys, As requested I've uploaded a Pdf version of my logo. Hopefully this help. Thanks

Industry/Entity Type

Business

Contact Information for Business Card

Name: Owen Wexcombe
Phone: 0471 385 962

Residential & Commercial
Fully Insured

Font styles to use
Serif
Sans Serif

Requirements
Must have
• Name must be all lower case "wexcombe roof plumbing"
Nice to have
• Stick with Logo Colours

```html
<!DOCTYPE html>
<html lang="en">
<head>
<meta charset="utf-8">
<title>wexcombe roof plumbing — business card</title>
<link rel="stylesheet" href="https://fonts.googleapis.com/css2?family=Open+Sans:wght@400;600&display=swap">
<style>
  :root {
    --backdrop: #3b3532;
    --card: #0f0f10;
    --card-edge: #1c1c1e;
    --brand-blue: #2aa3de;
    --ink: #f2f2f2;
    --rule: #8d8d8d;
    --silver: #c9c9c9;
  }
  * { box-sizing: border-box; margin: 0; padding: 0; }
  html, body {
    width: 1200px; height: 814px; overflow: hidden;
    background: var(--backdrop);
    font-family: "Open Sans", sans-serif;
  }
  .stage {
    position: relative; width: 1200px; height: 814px;
    display: flex; align-items: center; justify-content: center; gap: 48px;
  }
  .card {
    position: relative; width: 520px; height: 316px;
    background: var(--card);
    border: 1px solid var(--card-edge);
    border-radius: 3px;
    box-shadow: 0 14px 30px rgba(0,0,0,.45);
    overflow: hidden;
  }

  /* front */
  .brand {
    position: absolute; top: 46px; right: 40px;
    display: flex; align-items: center; gap: 10px;
    color: var(--brand-blue);
    font-size: 25px; font-weight: 400; letter-spacing: .5px;
  }
  .brand-square { width: 14px; height: 14px; background: var(--brand-blue); }
  .divider {
    position: absolute; left: 140px; right: 40px; top: 150px;
    height: 1px; background: var(--rule);
  }
  .contact { position: absolute; left: 36px; top: 174px; color: var(--ink); }
  .contact-head { display: flex; align-items: center; gap: 10px; }
  .contact-name { color: var(--brand-blue); font-size: 21px; font-weight: 600; white-space: nowrap; }
  .contact-head .rule { width: 150px; height: 1px; background: var(--rule); margin-top: 6px; }
  .contact-role { font-size: 15px; margin-top: 2px; }
  .contact-list { list-style: none; margin-top: 12px; font-size: 14px; }
  .contact-list li { display: flex; align-items: center; gap: 10px; margin-top: 4px; }
  .contact-list svg { width: 14px; height: 14px; fill: var(--brand-blue); flex: none; }

  /* back */
  .back-mark {
    position: absolute; top: 88px; left: 0; right: 0;
    display: flex; justify-content: center; align-items: center; gap: 12px;
    color: var(--silver); font-size: 28px; font-weight: 400; letter-spacing: 1px;
  }
  .back-mark .brand-square { background: var(--silver); width: 16px; height: 16px; }
  .services {
    position: absolute; left: 0; right: 0; bottom: 64px;
    display: flex; justify-content: center; gap: 8px;
    list-style: none; color: var(--ink); font-size: 14px;
  }
  .services li + li::before { content: "•"; color: var(--brand-blue); margin-right: 8px; }
</style>
</head>
<body>
<main class="stage">
  <section class="card card-front" aria-label="Business card front">
    <div class="brand"><span class="brand-square"></span><span>wexcombe roof plumbing</span></div>
    <div class="divider"></div>
    <div class="contact">
      <div class="contact-head"><span class="contact-name">Owen Wexcombe</span><span class="rule"></span></div>
      <p class="contact-role">CEO/Founder</p>
      <ul class="contact-list">
        <li>
          <svg viewBox="0 0 24 24" aria-hidden="true"><path d="M6.6 10.8a15.1 15.1 0 0 0 6.6 6.6l2.2-2.2c.3-.3.7-.4 1-.2 1.1.4 2.3.6 3.6.6.6 0 1 .4 1 1V20c0 .6-.4 1-1 1C10.6 21 3 13.4 3 4c0-.6.4-1 1-1h3.5c.6 0 1 .4 1 1 0 1.3.2 2.5.6 3.6.1.3 0 .7-.2 1z"/></svg>
          <span>0471 385 962</span>
        </li>
        <li>
          <svg viewBox="0 0 24 24" aria-hidden="true"><path d="M2 5h20v14H2z M2 5l10 8 10-8" /></svg>
          <span>owenwexcomberoofing@mailnest.example</span>
        </li>
      </ul>
    </div>
  </section>

  <section class="card card-back" aria-label="Business card back">
    <div class="back-mark"><span class="brand-square"></span><span>wexcombe roof plumbing</span></div>
    <ul class="services">
      <li>Fully Insured</li>
      <li>Residential &amp; Commercial</li>
      <li>Re-roof &amp; New Construction</li>
    </ul>
  </section>
</main>
</body>
</html>
```